Harborview Behavioral and Community Services

Intellectual Developmental Disabilities, Group Homes, Residential Homes and Substance Abuse Residential facilities

Target Market(s)

Adults 18-59 male and female autism, developmental disabilities and mental health

Industry/Entity Type

Intellectual Development Disabilities, Autism, Applied Behavioral Analysis, Mental Health, Substance Abuse

Coding

Coded - Design and coding required

Number of Pages Required

5+ page

Font styles to use
Serif

Colors
0054AA
0677BA
7BADD7
CADEEF
E8F1F8

Requirements
Should not have
• Not specified

```html
<!DOCTYPE html>
<html lang="en">
<head>
<meta charset="utf-8">
<title>Harborview Behavioral and Community Services</title>
<link href="https://fonts.googleapis.com/css2?family=Playfair+Display:wght@600;700&family=Poppins:wght@400;500;600;700&display=swap" rel="stylesheet">
<style>
:root{
  --blue:#0054AA;
  --blue-mid:#0677BA;
  --blue-soft:#7BADD7;
  --blue-pale:#CADEEF;
  --blue-mist:#E8F1F8;
  --navy:#0a3f8a;
  --ink:#222;
  --muted:#555;
  --white:#fff;
  --star:#f08a24;
  --map:#4499f0;
}
*{margin:0;padding:0;box-sizing:border-box}
html,body{width:1200px;height:5055px;overflow:hidden}
body{position:relative;font-family:"Poppins",sans-serif;color:var(--ink);background:var(--white)}
.abs{position:absolute}
.btn{display:inline-flex;align-items:center;gap:8px;background:var(--blue);color:var(--white);font-weight:700;font-size:12px;border-radius:26px;text-transform:uppercase;justify-content:center}
.btn .dot{width:11px;height:11px;border-radius:50%;background:var(--white);position:relative}
.btn .dot::after{content:"";position:absolute;left:3px;top:3px;border-left:5px solid var(--blue);border-top:2.5px solid transparent;border-bottom:2.5px solid transparent}

.topbar{left:0;top:0;width:1200px;height:40px;background:var(--blue);color:var(--white);font-size:11px;font-weight:700}
.topbar .links{left:111px;top:12px;letter-spacing:.2px}
.topbar .phone{right:110px;top:10px;font-size:15px;display:flex;align-items:center;gap:10px}
.header{left:0;top:40px;width:1200px;height:100px;background:var(--white)}
.brand{left:111px;top:32px;display:flex;align-items:center;gap:10px}
.brand .mark{width:30px;height:30px;border-radius:50%;background:var(--blue)}
.brand .name{font-family:"Playfair Display",serif;font-weight:700;font-size:22px;color:var(--navy);line-height:1}
.nav{left:488px;top:44px;display:flex;gap:22px;font-size:11.5px;font-weight:700;color:#111}
.contact-btn{left:926px;top:26px;width:162px;height:46px}

.hero{left:0;top:140px;width:1200px;height:600px}
.hero-photo{left:0;top:0;width:1200px;height:600px;background:linear-gradient(100deg,#3a3a3a 0%,#6a5a48 45%,#b0763a 70%,#d9973f 85%,#6d5c4c 100%)}
.hero h1{left:111px;top:102px;color:var(--white);font-family:"Playfair Display",serif;font-size:40px;font-weight:700;line-height:1.1}
.hero h1 small{display:block;font-size:28px;line-height:1.5;font-weight:600}
.hero .tag{left:111px;top:270px;color:var(--white);font-weight:700;font-size:15px}
.hero .cta{left:111px;top:324px;width:254px;height:44px}

.about-ring{left:113px;top:808px;width:454px;height:454px;border-radius:50%;border:7px solid var(--blue);border-right-color:transparent;border-top-color:transparent;transform:rotate(10deg)}
.about-photo{left:128px;top:815px;width:434px;height:434px;border-radius:50%;background:linear-gradient(135deg,#a99a85,#5a4a3e 50%,#c9bfb1)}
.h2{font-family:"Playfair Display",serif;font-weight:700;color:var(--blue);font-size:34px;letter-spacing:.5px}
.about h2{left:643px;top:855px}
.about .copy{left:643px;top:918px;width:446px;font-size:13px;line-height:24px;color:#333}
.about .copy p+p{margin-top:14px}
.about .more{left:643px;top:1193px;width:168px;height:44px}

.section-mark{width:30px;height:30px;border-radius:50%;background:var(--white)}
.services-title{left:0;top:1510px;width:1200px;text-align:center}
.mark-s{left:585px;top:1458px}
.svc{top:1620px;width:274px;height:280px;background:var(--white);border-radius:26px 26px 0 26px;text-align:center;padding:82px 26px 0}
.svc.active{background:transparent;border:3px solid var(--white);color:var(--white)}
.svc .ic{position:absolute;left:50%;top:-40px;transform:translateX(-50%);width:92px;height:92px;border-radius:50%;background:linear-gradient(135deg,var(--blue),var(--blue-mid));display:flex;align-items:center;justify-content:center;border:4px solid var(--white)}
.svc.active .ic{background:var(--white)}
.svc h3{font-family:"Playfair Display",serif;font-size:14px;font-weight:700;color:#222;line-height:1.5}
.svc.active h3{color:var(--white)}
.svc p{font-size:12.5px;line-height:22px;color:#333;margin-top:14px}
.svc.active p{color:var(--white)}
.svc .go{position:absolute;left:50%;bottom:26px;transform:translateX(-50%);width:20px;height:20px;border-radius:50%;background:var(--blue)}
.svc.active .go{background:var(--white)}
.svc .go::after{content:"";position:absolute;left:8px;top:5px;border-left:6px solid var(--white);border-top:5px solid transparent;border-bottom:5px solid transparent}
.svc.active .go::after{border-left-color:var(--blue)}
.arrow{top:1745px;width:34px;height:34px;border-radius:50%;background:var(--white)}

.mark-f{left:585px;top:2158px;background:var(--blue)}
.find-title{left:0;top:2205px;width:1200px;text-align:center}
.find-title span{color:var(--ink)}
.find-sub{left:280px;top:2275px;width:640px;text-align:center;font-size:13px;line-height:24px;color:#333}
.field{top:2355px;height:56px;border:1px solid #ccc;border-radius:28px;font-size:13px;color:#444;padding:19px 26px;background:var(--white)}
.search{left:824px;top:2357px;width:54px;height:54px;border-radius:50%;background:var(--blue)}
.map{left:265px;top:2440px;width:780px;height:490px;border-radius:24px;background:linear-gradient(135deg,#5aa6f2,var(--map) 55%,#3a8ee6)}

.mark-t{left:585px;top:3090px}
.testi-title{left:0;top:3145px;width:1200px;text-align:center}
.testi{top:3245px;width:345px;color:var(--white);font-size:12.5px;line-height:23px}
.testi.active{border:3px solid var(--white);border-radius:8px;padding:40px 30px 24px;width:400px;top:3240px}
.testi .who{display:flex;align-items:center;gap:14px;font-weight:700;font-size:13px;margin-bottom:14px}
.testi.active .who{position:absolute;top:-24px;left:30px}
.avatar{width:74px;height:74px;border-radius:50%;border:3px solid var(--white);background:linear-gradient(135deg,#c7a58a,#8a6a55)}
.stars{color:var(--star);letter-spacing:2px;font-size:14px}

.mark-b{left:585px;top:3722px;background:var(--blue)}
.blog-title{left:0;top:3770px;width:1200px;text-align:center}
.post{top:3835px;width:316px;height:382px;background:var(--white);box-shadow:0 2px 14px rgba(0,0,0,.12);border-radius:4px;text-align:center}
.post.active{border:2px solid #666;box-shadow:none}
.post .ph{margin:8px;height:197px}
.post h4{font-size:15px;font-weight:700;line-height:24px;margin:18px 22px 0;color:#222}
.post p{font-size:13px;line-height:23px;color:#555;margin:8px 22px 0}
.post a{display:inline-block;margin-top:6px;color:var(--blue);font-size:13px;line-height:20px;text-decoration:underline}

.footer-bg{left:0;top:4425px;width:1200px;height:630px;background:var(--blue-pale)}
.cta-box{left:111px;top:4315px;width:978px;height:325px;background:linear-gradient(100deg,var(--blue),var(--blue-mid));text-align:center;color:var(--white);padding-top:78px}
.cta-box h2{font-family:"Playfair Display",serif;font-size:33px;font-weight:700;letter-spacing:.3px}
.cta-box p{font-size:13px;line-height:24px;width:760px;margin:14px auto 0}
.cta-box .ghost{margin-top:28px;border:1px solid var(--white);background:transparent;width:302px;height:44px}
.cta-box .ghost .dot::after{border-left-color:var(--blue)}
.fcol{top:4690px;font-size:12px;line-height:21.5px;color:#222}
.fcol h5{font-size:12px;font-weight:700;margin-bottom:10px}
.news-in{left:884px;top:4773px;width:202px;height:44px;border-radius:22px;background:var(--white);font-size:12px;color:#555;padding:13px 24px}
.news-btn{left:884px;top:4830px;width:202px;height:44px}
.rule{left:111px;top:4935px;width:978px;height:1px;background:#b5c9dc}
.copyright{left:0;top:4955px;width:1200px;text-align:center;font-size:12px}
.code{left:1110px;top:4955px;font-size:12px}
</style>
</head>
<body>

<div class="abs topbar">
  <div class="abs links">DONATE &nbsp;&nbsp;|&nbsp;&nbsp; JOIN OUR TEAM &nbsp;&nbsp;|&nbsp;&nbsp; ABUSE PREVENTION</div>
  <div class="abs phone">
    <svg width="14" height="14" viewBox="0 0 24 24"><path fill="#fff" d="M6.6 10.8a15 15 0 0 0 6.6 6.6l2.2-2.2c.3-.3.7-.4 1-.2 1.1.4 2.3.6 3.6.6.6 0 1 .4 1 1V20c0 .6-.4 1-1 1A17 17 0 0 1 3 4c0-.6.4-1 1-1h3.5c.6 0 1 .4 1 1 0 1.3.2 2.5.6 3.6.1.3 0 .7-.2 1z"/></svg>
    +1 (555) 010 2040
  </div>
</div>

<header class="abs header">
  <div class="abs brand"><span class="mark"></span><span class="name">HARBORVIEW</span></div>
  <nav class="abs nav"><span>OUR SERVICES</span><span>OUR LOCATIONS</span><span>ABOUT US</span><span>FOUNDATION</span></nav>
  <div class="abs btn contact-btn">CONTACT US</div>
</header>

<section class="abs hero">
  <div class="abs hero-photo" role="img" aria-label="Photo of a smiling young woman in an orange top at a community learning centre"></div>
  <svg class="abs" style="left:0;top:430px" width="1200" height="175" viewBox="0 0 1200 175">
    <path d="M0 80 C300 175 700 190 1200 60 L1200 175 L0 175 Z" fill="#fff"/>
    <path d="M0 80 C300 175 700 190 1200 60 L1200 40 C700 175 300 165 0 60 Z" fill="#0054AA"/>
  </svg>
  <h1 class="abs">EMPOWERING COMMUNITIES<small>WITH INNOVATIVE CARE AND<br>EDUCATION SOLUTIONS</small></h1>
  <div class="abs tag">PUTTING OUR HEART AND SOUL INTO EXCEPTIONAL CARE</div>
  <div class="abs btn cta">GET A FREE CONSULTATION <span class="dot"></span></div>
</section>

<section class="about">
  <div class="abs about-ring"></div>
  <div class="abs about-photo" role="img" aria-label="Photo of a caregiver and a young man reviewing paperwork together"></div>
  <h2 class="abs h2">ABOUT US</h2>
  <div class="abs copy">
    <p>Lorem ipsum dolor sit amet, consectetur adipiscing elit, sed do eiusmod tempor incididunt ut labore et dolore magna aliqua. Ut enim ad minim veniam, quis nostrud exercitation ullamco laboris nisi ut aliquip ex ea commodo consequat. Duis aute irure dolor in reprehenderit in voluptate velit esse cillum dolore eu fugiat nulla pariatur. Excepteur sint occaecat cupidatat non proident, sunt in culpa qui officia deserunt mollit anim id est laborum.</p>
    <p>Lorem ipsum dolor sit amet, consectetur adipiscing elit, sed do eiusmod tempor incididunt ut labore et dolore magna aliqua. Ut enim ad minim veniam, quis nostrud exercitation</p>
  </div>
  <div class="abs btn more">LEARN MORE <span class="dot"></span></div>
</section>

<section>
  <svg class="abs" style="left:0;top:1340px" width="1200" height="755" viewBox="0 0 1200 755">
    <defs><linearGradient id="g1" x1="0" x2="1"><stop offset="0" stop-color="#0054AA"/><stop offset="1" stop-color="#0a62b8"/></linearGradient></defs>
    <path d="M0 60 C350 -20 800 10 1200 60 L1200 700 C800 760 350 680 0 610 Z" fill="url(#g1)"/>
    <path d="M0 65 C350 -10 800 20 1200 70 L1200 75 C800 25 350 0 0 72 Z" fill="#fff"/>
    <path d="M0 605 C350 700 800 760 1200 700 L1200 715 C800 770 350 715 0 612 Z" fill="#fff" opacity=".9"/>
  </svg>
  <div class="abs section-mark mark-s"></div>
  <h2 class="abs h2 services-title" style="color:#fff">OUR SERVICES</h2>
  <div class="abs arrow" style="left:86px"></div>
  <div class="abs arrow" style="left:1080px"></div>
  <div class="abs svc" style="left:147px">
    <div class="ic"><svg width="40" height="40" viewBox="0 0 40 40" fill="none" stroke="#fff" stroke-width="2"><circle cx="20" cy="20" r="15"/><path d="M12 24h16M14 18l6-6 6 6"/></svg></div>
    <h3>Addiction Recovery Services</h3>
    <p>Providing support on your road to recovery, with counseling, development of life skills, and relapse prevention.</p>
    <span class="go"></span>
  </div>
  <div class="abs svc active" style="left:460px">
    <div class="ic"><svg width="40" height="40" viewBox="0 0 40 40" fill="none" stroke="#0054AA" stroke-width="2"><path d="M10 30V20a10 10 0 1 1 14 9v5"/><rect x="16" y="12" width="8" height="8"/></svg></div>
    <h3>Autism</h3>
    <p>Providing support on your road to recovery, with counseling, development of life skills, and relapse prevention.</p>
    <span class="go"></span>
  </div>
  <div class="abs svc" style="left:780px">
    <div class="ic"><svg width="40" height="40" viewBox="0 0 40 40" fill="none" stroke="#fff" stroke-width="2"><circle cx="20" cy="8" r="3"/><path d="M19 13v10h9l4 8M16 19a8 8 0 1 0 9 12"/></svg></div>
    <h3>Intellectual and Development Disabilities</h3>
    <p style="margin-top:8px">Providing support on your road to recovery, with counseling, development of life skills, and relapse prevention.</p>
    <span class="go"></span>
  </div>
</section>

<section>
  <div class="abs section-mark mark-f"></div>
  <h2 class="abs h2 find-title">FIND SERVICES <span>NEAR YOU</span></h2>
  <p class="abs find-sub">Select a service below to find out if Crestline can help with your developmental, behavioral health and educational needs.</p>
  <div class="abs field" style="left:321px;width:318px">Related Service<span style="position:absolute;right:30px;top:17px">&#8964;</span></div>
  <div class="abs field" style="left:644px;width:168px">Zip code</div>
  <div class="abs search"><svg style="margin:17px" width="20" height="20" viewBox="0 0 20 20" fill="none" stroke="#fff" stroke-width="2.5"><circle cx="8" cy="8" r="6"/><path d="M13 13l5 5"/></svg></div>
  <div class="abs map" role="img" aria-label="Interactive map of the United States with selectable states"></div>
</section>

<section>
  <svg class="abs" style="left:0;top:2985px" width="1200" height="670" viewBox="0 0 1200 670">
    <defs><linearGradient id="g2" x1="0" x2="1"><stop offset="0" stop-color="#0054AA"/><stop offset="1" stop-color="#0677BA"/></linearGradient></defs>
    <path d="M0 40 C400 -10 800 -10 1200 30 L1200 620 C800 660 350 590 0 540 Z" fill="url(#g2)"/>
    <path d="M0 48 C400 0 800 0 1200 40 L1200 45 C800 8 400 8 0 56 Z" fill="#fff"/>
    <path d="M0 535 C350 600 800 670 1200 620 L1200 630 C800 675 350 610 0 545 Z" fill="#fff" opacity=".9"/>
  </svg>
  <div class="abs section-mark mark-t"></div>
  <h2 class="abs h2 testi-title" style="color:#fff">OUR TESTIMONIALS</h2>
  <div class="abs testi" style="left:32px">
    <div class="who"><span class="avatar" role="img" aria-label="Reviewer portrait"></span>ANTONY MK <span class="stars">★★★★★</span></div>
    Lorem ipsum dolor sit amet, consectetur adipiscing elit, sed do eiusmod tempor incididunt ut labore et dolore magna aliqua. Ut enim ad minim veniam, quis nostrud exercitation ullamco laboris nisi ut aliquip ex ea commodo consequat.
  </div>
  <div class="abs testi active" style="left:400px">
    <div class="who"><span class="avatar" role="img" aria-label="Reviewer portrait"></span>JHON SMITH <span class="stars">★★★★★</span></div>
    Lorem ipsum dolor sit amet, consectetur adipiscing elit, sed do eiusmod tempor incididunt ut labore et dolore magna aliqua. Ut enim ad minim veniam, quis nostrud exercitation ullamco laboris nisi ut aliquip ex ea commodo consequat.
  </div>
  <div class="abs testi" style="left:837px">
    <div class="who"><span class="avatar" role="img" aria-label="Reviewer portrait"></span>DANNIEL CX <span class="stars">★★★★★</span></div>
    Lorem ipsum dolor sit amet, consectetur adipiscing elit, sed do eiusmod tempor incididunt ut labore et dolore magna aliqua. Ut enim ad minim veniam, quis nostrud exercitation ullamco laboris nisi ut aliquip ex ea commodo consequat.
  </div>
</section>

<section>
  <div class="abs section-mark mark-b"></div>
  <h2 class="abs h2 blog-title">OUR BLOG</h2>
  <article class="abs post" style="left:107px">
    <div class="ph" role="img" aria-label="Photo of a caregiver laughing with a man in a wheelchair" style="background:linear-gradient(135deg,#e8dccb,#b09478 60%,#6b5a4d)"></div>
    <h4>What's Happening in IDD Services?</h4>
    <p>Lorem ipsum dolor sit amet, consectetur adipiscing elit, sed do</p>
  </article>
  <article class="abs post active" style="left:442px">
    <div class="ph" role="img" aria-label="Photo of a family playing together at a playground" style="background:linear-gradient(135deg,#6b4a3a,#c08a5a 50%,#3e5a4a)"></div>
    <h4>Children and Family Services Networking Events</h4>
    <p>Lorem ipsum dolor sit amet, consectetur adipiscing elit, sed do eiusm</p>
    <a>View More</a>
  </article>
  <article class="abs post" style="left:777px">
    <div class="ph" role="img" aria-label="Photo of two boys playing a board game" style="background:linear-gradient(135deg,#8a3a2a,#c0603a 50%,#3a2a22)"></div>
    <h4>Save the Date for the 2025 Bowling Tournament</h4>
    <p>Lorem ipsum dolor sit amet, consectetur adipiscing elit, sed do</p>
  </article>
</section>

<div class="abs footer-bg"></div>
<section class="abs cta-box">
  <h2>HELPING YOU REACH YOUR FULLEST POTENTIAL</h2>
  <p>We are leading developmental, behavioral health, and education non-profit provider offering a wide range of services for individuals and communities across the country.</p>
  <div class="btn ghost">FIND OUT WHAT MAKES UNIQUE <span class="dot"></span></div>
</section>

<footer>
  <div class="abs fcol" style="left:111px"><h5>IMPORTANAT LINKS</h5>About Us<br>Our News<br>Meet Our Team!<br>Our Partners<br>Our Accreditations<br>Upcoming Events<br>Annual Reports</div>
  <div class="abs fcol" style="left:368px"><h5>OUR FOUNDATION</h5>Ways to Give<br>Foundation Board<br>Employee Benefits<br>Hiring Events</div>
  <div class="abs fcol" style="left:599px"><h5>OUR LINKS</h5>Employee Portal<br>Outlook Webmail<br>Password Reset<br>Crestline Store<br>Media Resources<br>Crestline Brand Guide<br>TCR-MRF<br>Sitemap</div>
  <div class="abs fcol" style="left:884px;width:210px"><h5>STAY UPDATED</h5>Be in the know with our monthly newsletter!</div>
  <div class="abs news-in">Enter Email</div>
  <div class="abs btn news-btn">SUBMIT</div>
  <div class="abs rule"></div>
  <div class="abs copyright">Copyright@2025.All Rights Reserved</div>
  <div class="abs code">C72</div>
</footer>

</body>
</html>
```